Business Card Design

A business card design must match as a cleaning company.
We do house cleaning, office, cafe , function center , club and so on.

Industry/Entity Type

House

Contact Information for Business Card

Silver Fern cleaning services
Marla Voss
Director
0429385716
1300 862 419
Silverfern.cleaning@examplemail.com

```html
<!DOCTYPE html>
<html lang="en">
<head>
<meta charset="utf-8">
<title>Silver Fern Cleaning Services – Business Card</title>
<link rel="stylesheet" href="https://fonts.googleapis.com/css2?family=Arimo:wght@400;700&display=swap">
<style>
  :root {
    --backdrop: #c0c0c0;
    --card: #ffffff;
    --band-light: #5cc0d6;
    --band-mid: #00a3c2;
    --band-deep: #007d82;
    --ink: #222222;
    --accent: #9aba4c;
    --divider: #e2ead0;
  }
  * { margin: 0; padding: 0; box-sizing: border-box; }
  html, body {
    width: 1200px;
    height: 1000px;
    overflow: hidden;
    background: var(--backdrop);
    font-family: "Arimo", Arial, sans-serif;
    color: var(--ink);
  }
  .card {
    position: absolute;
    left: 169px;
    top: 231px;
    width: 862px;
    height: 532px;
    background: var(--card);
  }
  .card__band {
    position: absolute;
    left: 0; top: 0;
    width: 862px;
    height: 331px;
    background: linear-gradient(90deg, var(--band-light) 0%, var(--band-mid) 20%, #0098b8 55%, var(--band-deep) 100%);
  }
  .card__band-glow {
    position: absolute;
    left: 0; top: 0;
    width: 300px;
    height: 331px;
    background: radial-gradient(ellipse at 20% 40%, rgba(255,255,255,0.18), rgba(255,255,255,0) 70%);
  }
  .brand {
    position: absolute;
    left: 62px;
    top: 378px;
    display: flex;
    align-items: center;
    gap: 18px;
  }
  .brand__dot {
    width: 34px;
    height: 34px;
    border-radius: 50%;
    background: var(--accent);
  }
  .brand__name {
    font-weight: 400;
    color: var(--ink);
    line-height: 1;
  }
  .brand__name-main { display: block; font-size: 46px; }
  .brand__name-sub { display: block; font-size: 16px; letter-spacing: 4px; margin-top: 6px; }
  .card__divider {
    position: absolute;
    left: 468px;
    top: 365px;
    width: 1px;
    height: 108px;
    background: var(--divider);
  }
  .contact {
    position: absolute;
    left: 495px;
    top: 374px;
  }
  .contact__person { font-size: 20px; margin-bottom: 12px; }
  .contact__name { font-weight: 700; }
  .contact__role { font-weight: 400; }
  .contact__line {
    display: flex;
    align-items: center;
    gap: 10px;
    font-size: 18px;
    height: 29px;
  }
  .contact__icon { width: 24px; display: flex; justify-content: center; }
</style>
</head>
<body>
  <div class="card">
    <div class="card__band">
      <div class="card__band-glow"></div>
    </div>

    <div class="brand">
      <span class="brand__dot"></span>
      <span class="brand__name">
        <span class="brand__name-main">Silver Fern</span>
        <span class="brand__name-sub">Cleaning Services</span>
      </span>
    </div>

    <div class="card__divider"></div>

    <div class="contact">
      <p class="contact__person"><span class="contact__name">Marla Voss</span> <span class="contact__role">( Director )</span></p>
      <p class="contact__line">
        <span class="contact__icon">
          <svg width="14" height="22" viewBox="0 0 14 22" aria-hidden="true">
            <rect x="1" y="1" width="12" height="20" rx="2" fill="none" stroke="#9aba4c" stroke-width="2"/>
            <rect x="4" y="16" width="6" height="2" fill="#9aba4c"/>
          </svg>
        </span>
        0429385716 , 1300 862 419
      </p>
      <p class="contact__line">
        <span class="contact__icon">
          <svg width="26" height="17" viewBox="0 0 26 17" aria-hidden="true">
            <rect x="0" y="0" width="26" height="17" rx="1.5" fill="#9aba4c"/>
            <path d="M1 1 L13 10 L25 1" fill="none" stroke="#ffffff" stroke-width="1.6"/>
          </svg>
        </span>
        Silverfern.cleaning@examplemail.com
      </p>
    </div>
  </div>
</body>
</html>
```